Simple
Garrick Holloway DDS, MS, PC
Orthodontics
Please Note I have four offices and need a business card for each. Below is the information for each office to be listed beside the logo on the business cards: Garrick Holloway DDS, MS Board Certified Orthodontist Salt Lake Office Cedar Hollow Professional Bldg 3815 South 700 East Suite F Salt Lake City, Utah 84117 801 439 2106 ghbraces.example Garrick Holloway DDS, MS Board Certified Orthodontist Harvest Ridge Office 1847 West Juniper Bend Drive Suite 140 Lehi, Utah 84043 801 592 3081 ghbraces.example Garrick Holloway DDS, MS Board Certified Orthodontist Kemmerer/ Diamondville Office 200 Mesa Lane Diamondville, Wyoming 83116 307 614 2839 ghbraces.example Garrick Holloway DDS, MS Board Certified Orthodontist American Fork Office 246 North 300 West American Fork, Utah 84003 801 683 1952 ghbraces.example
info@ghbraces.example
ghbraces.example
For the stationery I need the following: Letterhead: 2 Separate Letterheads with two office addresses per letterhead. Letterhead #1 to contain the following: Logo with these two addresses: Harvest Ridge Office 1847 West Juniper Bend Drive Suite 140 Lehi, Utah 84043 801 592 3081 American Fork Office 246 North 300 West American Fork, Utah 84003 801 683 1952 Also on the Letterhead at the bottom of the page the following should be placed on one line: Garrick Holloway DDS, MS Board Certified Orthodontist Letterhead #2 to contain the following: Logo plus these two addresses: Salt Lake Office Cedar Hollow Professional Bldg 3815 South 700 East Suite F Salt Lake City, Utah 84117 801 439 2106 Kemmerer/ Diamondville Office 200 Mesa Lane Diamondville, Wyoming 83116 307 614 2839 Also on the Letterhead at the bottom of the page should be placed the following on one line: Garrick Holloway DDS, MS Board Certified Orthodontist Envelopes: I need two letterhead envelopes: Letterhead Envelope #1 to contain Logo plus this return address: 1847 West Juniper Bend Drive Suite 140 Lehi, Utah 84043 Letterhead Envelope #2 to contain Logo plus this return address: Cedar Hollow Professional Bldg 3815 South 700 East Suite F Salt Lake City, Utah 84117 Other Envelopes: Billing Envelope is #10 Size with a window to contain Logo with this return address: 1847 West Juniper Bend Drive Suite 140 Lehi, Utah 84043 Remittance Envelope: Size 6 3/4 (3 5/8 inch by 6 1/2 inch), to contain blank return address location and the following address in the addressee location front center of envelope: Garrick Holloway DDS, MS, PC Orthodontics 1847 West Juniper Bend Drive Suite 140 Lehi, Utah 84043 The #10 billing Envelope and the # 6 3/4 Remittance envelopes are white. The Letterhead sheets and envelopes are Torvell papers, linen sheen, off white in color. Any questions pleas email. Thanks, GH

```html
<!DOCTYPE html>
<html lang="en">
<head>
<meta charset="utf-8">
<title>Garrick Holloway Orthodontics – Stationery</title>
<link rel="stylesheet" href="https://fonts.googleapis.com/css2?family=Lato:wght@400;700&display=swap">
<style>
  :root {
    --bg: #e6e3de;
    --paper: #fbfaf6;
    --white: #ffffff;
    --green: #7cc242;
    --green-dark: #5fa22c;
    --ink: #6b6b6b;
    --ink-soft: #9a9a9a;
    --swoosh: #8d8d8d;
    --label: #7a7a7a;
  }
  * { box-sizing: border-box; margin: 0; padding: 0; }
  html, body { width: 1200px; height: 650px; overflow: hidden; }
  body {
    position: relative;
    background: var(--bg);
    font-family: "Lato", Arial, sans-serif;
    color: var(--ink);
  }
  .piece {
    position: absolute;
    overflow: hidden;
    box-shadow: 0 4px 12px rgba(0,0,0,.18);
  }
  .size-label {
    position: absolute;
    font-size: 11px;
    font-weight: 700;
    color: var(--label);
  }
  .wordmark {
    display: flex;
    align-items: center;
    gap: 6px;
    color: var(--green);
    font-weight: 700;
    text-transform: uppercase;
    letter-spacing: .04em;
    line-height: 1.15;
    white-space: nowrap;
  }
  .wordmark-square {
    width: 10px; height: 10px;
    background: var(--green);
    flex: none;
  }
  .bottom-curve { position: absolute; left: 0; bottom: 0; width: 100%; }

  /* Letterhead */
  .letterhead { left: 40px; top: 160px; width: 340px; height: 440px; background: var(--paper); }
  .letterhead .wordmark { position: absolute; left: 20px; top: 30px; font-size: 9.5px; }
  .letterhead-offices {
    position: absolute; left: 196px; top: 24px;
    font-size: 6px; line-height: 1.45; color: var(--ink);
    white-space: nowrap;
  }
  .letterhead-offices p + p { margin-top: 5px; }
  .letterhead-footer {
    position: absolute; right: 16px; bottom: 8px;
    font-size: 9px; color: var(--white); letter-spacing: .02em;
  }
  .letterhead-footer span + span { margin-left: 14px; }

  /* #10 envelope */
  .envelope { left: 410px; top: 250px; width: 440px; height: 191px; background: var(--paper); }
  .envelope-flap { position: absolute; left: 0; top: 0; width: 100%; height: 38px; }
  .envelope .wordmark { position: absolute; left: 22px; top: 56px; font-size: 8.5px; }
  .envelope-return {
    position: absolute; left: 160px; top: 54px;
    font-size: 6.5px; line-height: 1.5; padding-left: 8px;
    border-left: 1px solid var(--ink-soft);
    white-space: nowrap;
  }
  .envelope-window {
    position: absolute; left: 292px; top: 112px; width: 124px; height: 42px;
    border-radius: 6px; background: #e7e7e7; border: 1px solid #d3d3d3;
  }

  /* Business card */
  .card { left: 880px; top: 50px; width: 290px; height: 166px; background: var(--white); }
  .card .wordmark { position: absolute; left: 24px; top: 18px; font-size: 11px; }
  .card-details {
    position: absolute; left: 24px; top: 58px;
    font-size: 6.8px; line-height: 1.45; color: var(--ink);
  }
  .card-details strong { color: var(--green-dark); }
  .card-web {
    position: absolute; right: 14px; bottom: 6px;
    font-size: 8px; color: var(--white);
  }

  /* Remittance envelope */
  .remit { left: 860px; top: 380px; width: 310px; height: 173px; background: var(--white); }
  .remit-address {
    position: absolute; left: 118px; top: 52px;
    font-size: 7.5px; line-height: 1.5; color: var(--ink);
  }
</style>
</head>
<body>

  <span class="size-label" style="left:40px; top:142px;">8x11 Letterhead</span>
  <article class="piece letterhead">
    <div class="wordmark"><span class="wordmark-square"></span><span>Garrick Holloway<br>Orthodontics</span></div>
    <div class="letterhead-offices">
      <p><strong>Harvest Ridge Office</strong><br>1847 West Juniper Bend Drive Suite 140<br>Lehi, Utah 84043<br>801 592 3081</p>
      <p><strong>American Fork Office</strong><br>246 North 300 West<br>American Fork, Utah 84003<br>801 683 1952</p>
      <p>ghbraces.example</p>
    </div>
    <svg class="bottom-curve" width="340" height="70" viewBox="0 0 340 70" aria-hidden="true">
      <path d="M0 40 Q170 10 340 22 L340 70 L0 70 Z" fill="var(--green)"/>
      <path d="M0 34 Q170 2 340 14" fill="none" stroke="var(--swoosh)" stroke-width="1.2"/>
    </svg>
    <p class="letterhead-footer"><span>Garrick Holloway DDS, MS</span><span>Board Certified Orthodontist</span></p>
  </article>

  <span class="size-label" style="left:620px; top:448px;">4.125x9.5 Envelope</span>
  <article class="piece envelope">
    <svg class="envelope-flap" width="440" height="38" viewBox="0 0 440 38" aria-hidden="true">
      <path d="M0 0 H440 V30 Q220 4 0 30 Z" fill="var(--green)"/>
    </svg>
    <div class="wordmark"><span class="wordmark-square"></span><span>Garrick Holloway<br>Orthodontics</span></div>
    <div class="envelope-return">1847 West Juniper Bend Drive<br>Suite 140<br>Lehi, Utah 84043</div>
    <div class="envelope-window"></div>
    <svg class="bottom-curve" width="440" height="34" viewBox="0 0 440 34" aria-hidden="true">
      <path d="M0 22 Q220 2 440 18 L440 34 L0 34 Z" fill="var(--green)"/>
      <path d="M0 16 Q220 -4 440 12" fill="none" stroke="var(--swoosh)" stroke-width="1"/>
    </svg>
  </article>

  <span class="size-label" style="left:1140px; top:32px;">2x3.5</span>
  <article class="piece card">
    <div class="wordmark"><span class="wordmark-square"></span><span>Garrick Holloway<br>Orthodontics</span></div>
    <div class="card-details">
      <strong>Garrick Holloway DDS, MS</strong><br>
      Board Certified Orthodontist<br>
      Salt Lake Office<br>
      Cedar Hollow Professional Bldg<br>
      3815 South 700 East Suite F<br>
      Salt Lake City, Utah 84117<br>
      801 439 2106
    </div>
    <svg class="bottom-curve" width="290" height="40" viewBox="0 0 290 40" aria-hidden="true">
      <path d="M0 28 Q145 0 290 10 L290 40 L0 40 Z" fill="var(--green)"/>
      <path d="M0 22 Q145 -6 290 4" fill="none" stroke="var(--swoosh)" stroke-width="1"/>
    </svg>
    <p class="card-web">ghbraces.example</p>
  </article>

  <span class="size-label" style="left:860px; top:362px;">3.75x6.5</span>
  <article class="piece remit">
    <div class="remit-address">
      Garrick Holloway DDS, MS, PC<br>
      Orthodontics<br>
      1847 West Juniper Bend Drive<br>
      Suite 140<br>
      Lehi, Utah 84043
    </div>
    <svg class="bottom-curve" width="310" height="34" viewBox="0 0 310 34" aria-hidden="true">
      <path d="M0 20 Q155 2 310 16 L310 34 L0 34 Z" fill="var(--green)"/>
      <path d="M0 14 Q155 -4 310 10" fill="none" stroke="var(--swoosh)" stroke-width="1"/>
    </svg>
  </article>

</body>
</html>
```